I just need to get that same logo on the business card but with different word. “Marlow Tow and Lease”

Name: Dale K
Number: 4752869014
Email: marlowtow@fennmail.test

On the back, can we di just the logo and marlow tow and lease around it.

If possible a black card with the gold storefront type font that you used before, would be amazing. I attached the original logo just in case.

Target Market(s)

Roadside assistance

Industry/Entity Type

Repair/ roadside

Contact Information for Business Card

Name, email, phone number

Requirements
Must have
• Everything in description
Nice to have
• Nice big logo

```html
<!DOCTYPE html>
<html lang="en">
<head>
<meta charset="utf-8">
<title>Marlow Tow and Lease — Business Card</title>
<link href="https://fonts.googleapis.com/css2?family=Marcellus&family=Montserrat:wght@400&display=swap" rel="stylesheet">
<style>
  :root {
    --backdrop: #262626;
    --card: #1b1b1b;
    --gold: #c9974a;
    --ink-light: #efefef;
    --emboss: #242424;
    --pattern-light: #2c2c2c;
    --pattern-dark: #171717;
  }
  * { margin: 0; padding: 0; box-sizing: border-box; }
  html, body {
    width: 1200px;
    height: 900px;
    overflow: hidden;
    background: var(--backdrop);
  }
  .canvas {
    width: 1200px;
    height: 900px;
    display: flex;
    flex-direction: column;
    align-items: center;
    justify-content: center;
    gap: 36px;
  }
  .card {
    position: relative;
    width: 700px;
    height: 400px;
    background: var(--card);
    box-shadow: 0 16px 40px rgba(0,0,0,0.5);
    overflow: hidden;
  }

  /* Front */
  .brand {
    position: absolute;
    display: flex;
    align-items: center;
    gap: 14px;
  }
  .card-front .brand { left: 48px; top: 44px; }
  .brand-square {
    width: 28px;
    height: 28px;
    background: var(--gold);
    flex: none;
  }
  .brand-name {
    font-family: "Marcellus", serif;
    font-size: 28px;
    letter-spacing: 1.5px;
    text-transform: uppercase;
    color: var(--gold);
    white-space: nowrap;
  }
  .holder {
    position: absolute;
    left: 48px;
    top: 168px;
  }
  .holder-name {
    font-family: "Marcellus", serif;
    font-size: 24px;
    color: var(--gold);
  }
  .holder-rule {
    width: 7px;
    height: 2px;
    background: var(--gold);
    margin-top: 8px;
  }
  .contacts {
    position: absolute;
    left: 48px;
    top: 228px;
    list-style: none;
    font-family: "Montserrat", sans-serif;
    font-size: 15px;
    color: var(--ink-light);
  }
  .contacts li {
    display: flex;
    align-items: center;
    gap: 10px;
    margin-bottom: 10px;
  }
  .contacts svg { width: 14px; height: 14px; fill: var(--gold); flex: none; }
  .emboss-name {
    position: absolute;
    right: 36px;
    bottom: 30px;
    width: 300px;
    font-family: "Marcellus", serif;
    font-size: 54px;
    line-height: 1.02;
    text-transform: uppercase;
    text-align: right;
    color: var(--emboss);
  }

  /* Back */
  .back-pattern {
    position: absolute;
    inset: 0;
    background: linear-gradient(135deg, var(--pattern-light), var(--pattern-dark) 55%, var(--pattern-light));
  }
  .card-back .brand { left: 48px; bottom: 40px; }
  .card-back .brand-name { font-size: 22px; }
  .card-back .brand-square { width: 22px; height: 22px; }
</style>
</head>
<body>
<main class="canvas">
  <section class="card card-front">
    <div class="brand">
      <span class="brand-square"></span>
      <span class="brand-name">Marlow Tow and Lease</span>
    </div>

    <div class="holder">
      <p class="holder-name">Dale K</p>
      <div class="holder-rule"></div>
    </div>

    <ul class="contacts">
      <li>
        <svg viewBox="0 0 24 24" aria-hidden="true"><path d="M6.6 10.8a15.1 15.1 0 0 0 6.6 6.6l2.2-2.2a1 1 0 0 1 1-.25 11.4 11.4 0 0 0 3.6.57 1 1 0 0 1 1 1V20a1 1 0 0 1-1 1A17 17 0 0 1 3 4a1 1 0 0 1 1-1h3.5a1 1 0 0 1 1 1c0 1.25.2 2.45.57 3.57a1 1 0 0 1-.25 1z"/></svg>
        <span>4752869014</span>
      </li>
      <li>
        <svg viewBox="0 0 24 24" aria-hidden="true"><path d="M2 5h20v14H2z"/></svg>
        <span>marlowtow@fennmail.test</span>
      </li>
    </ul>

    <p class="emboss-name">Marlow Tow and Lease</p>
  </section>

  <section class="card card-back">
    <div class="back-pattern" role="img" aria-label="Repeating gloss brand pattern, black on black"></div>
    <div class="brand">
      <span class="brand-square"></span>
      <span class="brand-name">Marlow Tow and Lease</span>
    </div>
  </section>
</main>
</body>
</html>
```